Thimble Nook web site

I have been running an online business for 6 years.
www.thimblenook.com.au I specialise in ribbons, buttons and unique craft materials. I sell online to individuals and shops with seperate retail and wholesale sites. The web page I'd like redesigned is my retail site.

It needs a clean, fresh look. I've recently had a new logo designed (thanks pixel harbour!) and want the web site to incorporate the new design and colour scheme of black and white. (new logo attached as a file)

I no longer want the page with the large image www.thimblenook.com.au I want to have the first page as the retail shop homepage.
http://www.thimblenook.com.au/index.php so this page needs to have all the links

I want to the look to be fresh, modern and clear. It needs to be quick to load.

Notes from my IT guru: They need to know that the following tend to remain static with just the content section changing on each page; Header Left column (but different in the cart) right column (if required) footer
Updates

Thanks for your designs. 1/3 of my users use mobile devices so please take that into consideration. I would like the logo to be incorporated into the design and be a prominent feature (most have just used it as a tiny image in the top left corner. I would like it to be larger and more prominent.  thanks                                   

Thanks to all the designers who have submitted. Can you please add  'Boutique craft supplies' near the logo. That is my tag line. Thanks

Target Market(s)

Crafty females of all ages

Industry/Entity Type

Business

Requirements
Must have
• links to;
blog
gallery
chatterloop
snapboardly
wholesale
space for an image which I change approx every 2 weeks
about Thimble Nook
contact
privacy policy
terms and conditions
newsletter sign up
shipping info
product search
Nice to have
• I am not sure if I want product images on the homepage? I have attached a few images.
Should not have
• not too much colour - I hate the green border I have now

```html
<!DOCTYPE html>
<html lang="en">
<head>
<meta charset="utf-8">
<title>Thimble Nook – Boutique craft supplies</title>
<link href="https://fonts.googleapis.com/css2?family=PT+Sans:ital,wght@0,400;0,700;1,400&family=PT+Sans+Narrow:wght@400;700&display=swap" rel="stylesheet">
<style>
:root{
  --page:#ebebeb;
  --panel:#f7f7f7;
  --white:#ffffff;
  --ink:#1a1a1a;
  --text:#333333;
  --muted:#666666;
  --card:#6a6a6a;
  --footer:#5b5b5b;
  --orange:#f7a21b;
  --orange-dark:#f08a00;
  --caption:rgba(70,70,70,.88);
}
*{box-sizing:border-box;margin:0;padding:0}
html,body{width:993px;height:1200px;overflow:hidden}
body{position:relative;background:linear-gradient(#f2f2f2,#e6e6e6 60%,#e9e9e9);font-family:"PT Sans",sans-serif;color:var(--text)}
.abs{position:absolute}

/* header */
.site-header{left:108px;top:3px;width:777px;height:125px;background:linear-gradient(#fff,#f0f0f0);border-radius:8px;box-shadow:0 2px 4px rgba(0,0,0,.15)}
.brand{left:22px;top:14px;display:flex;align-items:center;gap:12px}
.brand-dot{width:28px;height:28px;border-radius:50%;background:var(--ink);flex:none}
.brand-text{display:flex;flex-direction:column}
.brand-name{font-family:"PT Sans Narrow",sans-serif;font-weight:700;font-size:50px;line-height:54px;color:var(--ink)}
.brand-tagline{font-family:"PT Sans Narrow",sans-serif;font-size:16px;line-height:20px;color:#555;letter-spacing:.5px}
.util-links{right:22px;top:16px;display:flex;gap:10px;font-size:11px;color:#444;align-items:center}
.util-links .sep{color:#777}
.util-links svg{vertical-align:-2px;margin-right:4px}
.search{left:514px;top:52px;width:246px;height:27px;border:1px solid #ddd;background:#fff;display:flex}
.search input{flex:1;border:0;padding:0 10px;font:italic 11px "PT Sans",sans-serif;color:#777;background:transparent}
.search-btn{width:33px;background:var(--orange);display:flex;align-items:center;justify-content:center}
.main-nav{left:382px;top:92px;height:33px;display:flex;font-family:"PT Sans Narrow",sans-serif;font-size:15px;color:#222}
.main-nav a{display:block;height:33px;line-height:33px;color:inherit;text-decoration:none}
.main-nav .active{background:var(--ink);color:#fff;border-radius:6px 6px 0 0;width:79px;text-align:center}

/* hero */
.hero{left:108px;top:139px;width:777px;height:289px;border:3px solid #fff;border-radius:8px;overflow:hidden;box-shadow:0 1px 3px rgba(0,0,0,.2);
  background:linear-gradient(160deg,#eef0f2 0%,#d7e8f3 18%,#f3dbe8 38%,#d9c9ec 55%,#f8f0b8 72%,#dcefc8 88%,#eef0f2 100%)}
.hero-caption{left:1px;top:173px;width:258px;height:86px;background:var(--caption);color:#fff}
.hero-caption h2{position:absolute;left:19px;top:27px;font:400 19px "PT Sans Narrow",sans-serif;letter-spacing:-.2px}
.hero-arrows{position:absolute;right:12px;top:54px;font:700 22px "PT Sans Narrow",sans-serif;letter-spacing:6px}
.hero-shadow{left:125px;top:428px;width:743px;height:14px;background:radial-gradient(ellipse at top,rgba(0,0,0,.55),rgba(0,0,0,0) 70%)}

/* sidebar */
.side-box{background:var(--panel);border-radius:6px;box-shadow:0 0 3px rgba(0,0,0,.12)}
.categories{left:108px;top:447px;width:200px;height:419px}
.cat-head{position:absolute;left:7px;top:6px;width:186px;height:29px;background:#fff;border-radius:4px;box-shadow:0 0 2px rgba(0,0,0,.1);font-size:13px;color:#444;display:flex;align-items:center;padding-left:10px;gap:8px}
.cat-head i{width:9px;height:9px;background:#222;border-radius:2px;display:inline-block}
.cat-list{position:absolute;left:22px;top:45px;list-style:none;font-size:11px;color:#222}
.cat-list li{height:18.2px;line-height:18.2px}
.cat-list li::before{content:"›";display:inline-block;width:12px;color:#555}
.basket{left:108px;top:889px;width:200px;height:162px}
.basket h3{position:absolute;left:17px;top:10px;font:400 14px "PT Sans Narrow",sans-serif;color:#111}
.basket .empty{position:absolute;left:17px;top:40px;font:400 14px "PT Sans Narrow",sans-serif;color:#111}
.basket .cart-ico{position:absolute;left:138px;top:44px}
.basket .row{position:absolute;left:17px;font:400 12px "PT Sans Narrow",sans-serif;color:#111}
.btn-orange{background:linear-gradient(var(--orange),var(--orange-dark));border-radius:7px;color:#222;text-align:center}
.basket .btn-orange{position:absolute;left:34px;top:116px;width:128px;height:31px;line-height:31px;font:400 14px "PT Sans Narrow",sans-serif}

/* promo */
.promo{left:331px;top:447px;width:554px;height:128px;background:#f8f8f8;border-radius:6px;overflow:hidden}
.promo-image{position:absolute;left:0;top:0;width:346px;height:128px;background:linear-gradient(100deg,#b9636e 0%,#c98b92 30%,#d6c3c6 52%,#a9c97a 72%,#e0e6d6 100%)}
.promo-text{position:absolute;left:345px;top:8px;width:205px;font-family:"PT Sans Narrow",sans-serif;color:#111}
.promo-text .lead{font-size:13px;line-height:15px}
.promo-text .note{font-size:9px;line-height:15px;margin-top:1px;color:#222}

/* products */
.products-title{left:334px;top:593px;font:700 19px "PT Sans Narrow",sans-serif;color:#555}
.products-arrows{left:852px;top:598px;font:700 20px "PT Sans Narrow",sans-serif;color:#444;letter-spacing:6px}
.product{width:171px;height:194px;background:var(--card);border:1px solid #555;border-radius:3px;box-shadow:0 1px 2px rgba(0,0,0,.2)}
.product .photo{position:absolute;left:17px;top:17px;width:131px;height:85px;border:2px solid #9fd8d6;border-radius:4px}
.product p{position:absolute;left:6px;top:110px;width:160px;font-size:9px;line-height:13.2px;color:#f0f0f0;text-align:center}
.product .price{position:absolute;left:11px;top:158px;font:700 16px "PT Sans Narrow",sans-serif;color:#fff}
.product .add{position:absolute;left:89px;top:155px;width:64px;height:25px;line-height:25px;background:linear-gradient(#3a3a3a,#111);border-radius:4px;color:#fff;text-align:center;font:700 10px "PT Sans Narrow",sans-serif}

/* footer */
.site-footer{left:0;top:1070px;width:993px;height:130px;background:var(--footer);border-top:2px solid #777}
.site-footer h4{position:absolute;left:110px;top:26px;font:700 13px "PT Sans Narrow",sans-serif;color:#fff;letter-spacing:.3px}
.news-input{position:absolute;left:104px;top:56px;width:196px;height:30px;background:#fff;border-radius:4px;font-size:9px;color:#333;line-height:30px;padding-left:13px}
.subscribe{position:absolute;left:314px;top:58px;width:76px;height:27px;line-height:27px;border-radius:4px;background:linear-gradient(var(--orange),var(--orange-dark));color:#fff;text-align:center;font-size:13px}
.social{position:absolute;right:94px;top:30px;display:flex;gap:10px;align-items:center;font-size:9px;color:#e6e6e6}
.social a{display:flex;align-items:center;gap:4px;color:inherit;text-decoration:none}
.social a span{width:18px;height:18px;border-radius:2px;background:#8a8a8a;border:1px solid #9c9c9c;display:inline-block}
.foot-links{position:absolute;right:94px;top:79px;font-size:9px;color:#e6e6e6}
.copyright{position:absolute;right:94px;top:99px;font-size:9px;color:#e6e6e6}
</style>
</head>
<body>

<header class="site-header abs">
  <div class="brand abs">
    <span class="brand-dot"></span>
    <div class="brand-text"><span class="brand-name">Thimble Nook</span><span class="brand-tagline">Boutique craft supplies</span></div>
  </div>
  <nav class="util-links abs">
    <span><svg width="11" height="10" viewBox="0 0 11 10"><path d="M0 1h2l1.5 5h6l1-4H3" fill="none" stroke="#555" stroke-width="1.2"/><circle cx="4" cy="8.5" r="1" fill="#555"/><circle cx="9" cy="8.5" r="1" fill="#555"/></svg>Shopping Cart</span><span class="sep">|</span>
    <span><svg width="9" height="10" viewBox="0 0 9 10"><rect x=".5" y=".5" width="8" height="9" fill="none" stroke="#555"/><path d="M2 3h5M2 5h5M2 7h5" stroke="#555"/></svg>My Wish List</span><span class="sep">|</span>
    <span><svg width="10" height="10" viewBox="0 0 10 10"><rect x=".5" y=".5" width="9" height="9" fill="none" stroke="#555"/><path d="M2 5l2 2 4-5" fill="none" stroke="#555" stroke-width="1.3"/></svg>Check Out</span><span class="sep">|</span>
    <span><svg width="8" height="10" viewBox="0 0 8 10"><rect x="0" y="4" width="8" height="6" fill="#555"/><path d="M2 4V2.5a2 2 0 0 1 4 0V4" fill="none" stroke="#555"/></svg>Log Out</span>
  </nav>
  <form class="search abs"><input type="text" value="Search Thimble Nook" aria-label="Search"><span class="search-btn"><svg width="15" height="15" viewBox="0 0 15 15"><circle cx="6" cy="6" r="4.5" fill="none" stroke="#fff" stroke-width="2"/><path d="M9.5 9.5l4 4" stroke="#fff" stroke-width="2.4"/></svg></span></form>
  <nav class="main-nav abs">
    <a class="active" href="#">SHOP</a>
    <a href="#" style="margin-left:9px">WHOLESALE</a>
    <a href="#" style="margin-left:35px">GALLERY</a>
    <a href="#" style="margin-left:37px">BLOG</a>
    <a href="#" style="margin-left:35px">CONTACT US</a>
  </nav>
</header>

<section class="hero abs" role="img" aria-label="Photo of coiled pastel gingham ribbons in blue, pink, lilac, yellow and green">
  <div class="hero-caption abs">
    <h2>SPECIALISING IN UNIQUE RIBBONS</h2>
    <span class="hero-arrows">❬❭</span>
  </div>
</section>
<div class="hero-shadow abs"></div>

<aside class="categories side-box abs">
  <div class="cat-head"><i></i>Categories</div>
  <ul class="cat-list">
    <li>New Products</li><li>** Clearance **</li><li>Adhesives</li><li>Buttons</li><li>Card Kits</li><li>Chipboard</li><li>Christmas</li><li>Embellishments</li><li>Embossing Folders</li><li>Lace</li><li>Flowers and Leaves</li><li>inks, mists and masks</li><li>Paper</li><li>Ribbon Club</li><li>Ribbons</li><li>Ribbons - organza</li><li>Sequins</li><li>Staaps</li><li>Stickers</li><li>Washi tape</li>
  </ul>
</aside>

<aside class="basket side-box abs">
  <h3>Shopping Basket</h3>
  <div class="empty">Your basket is empty.</div>
  <svg class="cart-ico" width="12" height="11" viewBox="0 0 11 10"><path d="M0 1h2l1.5 5h6l1-4H3" fill="none" stroke="#555" stroke-width="1.2"/><circle cx="4" cy="8.5" r="1" fill="#555"/><circle cx="9" cy="8.5" r="1" fill="#555"/></svg>
  <div class="row" style="top:75px">Items in cart:&nbsp;&nbsp; 0</div>
  <div class="row" style="top:95px">Total:&nbsp;&nbsp; $0.00</div>
  <div class="btn-orange">View Basket</div>
</aside>

<section class="promo abs">
  <div class="promo-image" role="img" aria-label="Photo of pink, burgundy and green fabric flowers with pearl centres"></div>
  <div class="promo-text">
    <p class="lead">Paperleaf May Card Kit by Nora Whitfield<br>Postage rates (within Australia only)<br>Orders over $50 - Free postage<br>Orders under $50 - $6 postage charge</p>
    <p class="note">NO international postage without prior postage price agreement. Please do not order online if you do not have an Australian address.</p>
  </div>
</section>

<h2 class="products-title abs">Our Products</h2>
<div class="products-arrows abs">❬❭</div>

<article class="product abs" style="left:335px;top:636px"><div class="photo" role="img" aria-label="Vintage style patterned paper pack" style="background:linear-gradient(120deg,#e9e3cf,#c9c09a,#e8dcc0)"></div><p>Uenim ad minim veniam, quis laboris nisi utaliquip ex irurdolor into nisi utaliquip ex irurdolor into</p><span class="price">$127.00</span><span class="add">Add To Cart</span></article>
<article class="product abs" style="left:525px;top:636px"><div class="photo" role="img" aria-label="Black and white bicycle print washi tape" style="background:linear-gradient(120deg,#f2f2f2,#c8c8c8,#eeeeee)"></div><p>Uenim ad minim veniam, quis laboris nisi utaliquip ex irurdolor into nisi utaliquip ex irurdolor into</p><span class="price">$127.00</span><span class="add">Add To Cart</span></article>
<article class="product abs" style="left:718px;top:636px"><div class="photo" role="img" aria-label="Pink pom-pom trim" style="background:linear-gradient(120deg,#e5b3b3,#d48a8e,#e9c2c2)"></div><p>Uenim ad minim veniam, quis laboris nisi utaliquip ex irurdolor into nisi utaliquip ex irurdolor into</p><span class="price">$127.00</span><span class="add">Add To Cart</span></article>
<article class="product abs" style="left:335px;top:860px"><div class="photo" role="img" aria-label="Pink lace print washi tape" style="background:linear-gradient(120deg,#f3c8d8,#e05a92,#f0d7e0)"></div><p>Uenim ad minim veniam, quis laboris nisi utaliquip ex irurdolor into nisi utaliquip ex irurdolor into</p><span class="price">$127.00</span><span class="add">Add To Cart</span></article>
<article class="product abs" style="left:525px;top:860px"><div class="photo" role="img" aria-label="Black and gold decorative buttons" style="background:linear-gradient(120deg,#cfcfcf,#3a342a,#bdbdbd)"></div><p>Uenim ad minim veniam, quis laboris nisi utaliquip ex irurdolor into nisi utaliquip ex irurdolor into</p><span class="price">$127.00</span><span class="add">Add To Cart</span></article>
<article class="product abs" style="left:718px;top:860px"><div class="photo" role="img" aria-label="Green chevron washi tape" style="background:linear-gradient(120deg,#e9f3df,#8cc663,#e4eed9)"></div><p>Uenim ad minim veniam, quis laboris nisi utaliquip ex irurdolor into nisi utaliquip ex irurdolor into</p><span class="price">$127.00</span><span class="add">Add To Cart</span></article>

<footer class="site-footer abs">
  <h4>NEWSLETTER</h4>
  <div class="news-input">Enter Your Email id</div>
  <div class="subscribe">Subscribe</div>
  <nav class="social" aria-label="Social links">
    <a href="#"><span></span>chatterloop</a>
    <a href="#"><span></span>snapboardly</a>
    <a href="#" aria-label="Blog feed"><span></span></a>
    <a href="#" aria-label="Email us"><span></span></a>
  </nav>
  <div class="foot-links">About Thimble Nook | Contact Thimble Nook | Shipping Info | Privacy Policy | Terms &amp; Conditions</div>
  <div class="copyright">© 2013 thimblenook.com., All rights reserved</div>
</footer>

</body>
</html>
```